Velvet Heron Website

We need a website for our software / project management services company based in South Africa called "Velvet Heron". We provide professional services to high value clients in the public and private sectors.

The website must present a highly professional company that exudes quality and confidence.

The theme should be a highly professional subdued look with a fairly limited palette. The neutral tone should be slightly offset with the colours from the company logo. The website should not look dead though, and subtle colour highligting should provide a fresh vibrant feel.

Refer to the current website for general content (www.velvetheron-example.co.za) that may be used. We would also like to make use of social integration and google maps.
Updates

Thanks to all the designers that have participated so far and to those that are cooking something up at this very minute :-)

We have received a lot of designs with elements that we absolutely love. So now the hard work of refining these designs can begin.

We'll try and provide feedback on every design received so far ... and await the beautiful designs that we haven't received yet :-)

Good Luck!

Reason: After careful consideration we are extending the deadline to make small revisions to some of the designs and to select the top three designs. Thank you for everyone who has made a contribution so far - we have several designs that we like and selecting the best one is proving to be difficult :-)

Target Market(s)

The company deals mostly with other businesses, so mostly B2B.

Industry/Entity Type

Software

Requirements
Nice to have
• Social integration

```html
<!DOCTYPE html>
<html lang="en">
<head>
<meta charset="utf-8">
<title>Velvet Heron</title>
<link rel="stylesheet" href="https://fonts.googleapis.com/css2?family=Source+Sans+3:wght@400;600&family=Crimson+Text:wght@400;600&family=PT+Sans+Narrow&display=swap">
<style>
:root{
  --page:#ffffff;
  --frame-light:#e6e6e6;
  --frame-mid:#cfcfcf;
  --stage-top:#dedede;
  --stage-bottom:#5e5e5e;
  --nav-top:#8a8a8a;
  --nav-bottom:#4a4a4a;
  --nav-active:#a5a5a5;
  --nav-text:#f2f2f2;
  --brand-grey:#6f6f6f;
  --brand-green:#7cbd2a;
  --heading-blue:#1d5f9e;
  --body-blue:#1f64b0;
  --link-green:#3fe04a;
  --accent-red:#e02a2a;
  --ink:#1e1e1e;
  --badge:#6b3e22;
}
*{margin:0;padding:0;box-sizing:border-box}
html,body{width:1200px;height:1156px;overflow:hidden;background:var(--page)}
body{position:relative;font-family:"Source Sans 3",Arial,sans-serif;color:var(--ink)}

.main-nav{position:absolute;left:100px;top:88px;width:628px;height:63px;display:flex;
  border-radius:12px;overflow:hidden;background:linear-gradient(var(--nav-top),var(--nav-bottom));
  box-shadow:0 3px 5px rgba(0,0,0,.35)}
.main-nav a{display:flex;align-items:center;justify-content:center;color:var(--nav-text);
  text-decoration:none;font-size:16px;letter-spacing:.3px;border-right:2px solid #dcdcdc}
.main-nav a:last-child{border-right:none}
.main-nav a.is-active{background:linear-gradient(#b9b9b9,var(--nav-active) 50%,#7a7a7a)}

.brand{position:absolute;left:765px;top:60px;display:flex;align-items:center;gap:14px}
.brand-dot{width:34px;height:34px;border-radius:50%;background:var(--brand-green)}
.brand-name{font-size:58px;font-weight:600;color:var(--brand-grey);letter-spacing:-.5px}

.frame{position:absolute;left:39px;top:156px;width:1127px;height:1000px;
  background:linear-gradient(90deg,var(--frame-mid),var(--frame-light) 15%,var(--frame-light) 85%,var(--frame-mid))}
.stage{position:absolute;left:98px;top:165px;width:1011px;height:895px;
  background:linear-gradient(var(--stage-top),#bdbdbd 45%,var(--stage-bottom));
  box-shadow:0 0 4px rgba(0,0,0,.4)}

.hero{position:absolute;left:103px;top:173px;width:1002px;height:350px;
  background:linear-gradient(90deg,#ffffff,#f1f1f1 60%,#e4e4e4)}
.hero-text{position:absolute;left:63px;top:62px;font-family:"Crimson Text",Georgia,serif}
.hero-kicker{font-size:32px;line-height:1.1}
.hero-title{font-size:32px;line-height:1.35}
.hero-title strong{color:var(--accent-red);font-size:44px;font-weight:600}
.hero-copy{margin-top:18px;font-size:18.5px;line-height:27px;color:#2a2a2a}
.hero-photo{position:absolute;right:0;top:0;width:490px;height:350px;
  background:radial-gradient(circle at 40% 40%,#e9e9e9,#d9b59a 45%,#caa285 65%,#ececec 90%)}

.service{position:absolute;left:134px;width:501px;display:flex;flex-direction:column;
  background:linear-gradient(#d2d2d2,#9a9a9a);box-shadow:2px 3px 5px rgba(0,0,0,.45)}
.service h2{flex:none;height:36px;background:linear-gradient(#ffffff,#e6e6e6);color:var(--heading-blue);
  font-size:29px;font-weight:400;text-align:center;line-height:36px}
.service p{padding:9px 12px 0 12px;font-family:"PT Sans Narrow","Arial Narrow",sans-serif;
  font-size:12.6px;line-height:16px;color:var(--body-blue)}
.service .more{margin-top:auto;padding:0 12px 4px;font-family:"PT Sans Narrow","Arial Narrow",sans-serif;
  font-size:12.6px;line-height:16px;color:var(--link-green);text-decoration:none}
.service--dev{top:544px;height:149px}
.service--pm{top:717px;height:148px}
.service--consult{top:890px;height:149px}
.service--consult p{padding-top:7px}

.award{position:absolute;left:760px;top:625px;width:222px;height:222px;border-radius:50%;
  border:16px solid var(--badge);opacity:.85}

.social{position:absolute;left:725px;top:997px;display:flex;gap:27px}
.social span{width:44px;height:44px;border-radius:8px;background:linear-gradient(#fafafa,#b8b8b8);
  box-shadow:1px 2px 3px rgba(0,0,0,.4)}

.footer{position:absolute;left:98px;top:1077px;width:1011px;height:60px;background:var(--page);
  display:flex;align-items:center;justify-content:center;font-size:16px}
</style>
</head>
<body>
<nav class="main-nav">
  <a href="#" class="is-active" style="width:88px">HOME</a>
  <a href="#" style="width:98px">ABOUT US</a>
  <a href="#" style="width:123px">PPORTFOLIO</a>
  <a href="#" style="width:191px">PROFESSIONAL SERVICES</a>
  <a href="#" style="width:128px">CONTACT US</a>
</nav>

<div class="brand"><span class="brand-dot"></span><span class="brand-name">Velvet Heron</span></div>

<div class="frame"></div>
<div class="stage"></div>

<section class="hero">
  <div class="hero-text">
    <div class="hero-kicker">Delivering</div>
    <div class="hero-title"><strong>Integrated</strong> Solutions...</div>
    <p class="hero-copy">With experienced Architects, Designers and<br>Consultants we will deliver a solution that seamlessly<br>integrates to your Applications Framework.</p>
  </div>
  <div class="hero-photo" role="img" aria-label="Photo of a hand placing a red puzzle piece into a silver puzzle globe"></div>
</section>

<article class="service service--dev">
  <h2>Soft Development</h2>
  <p>Software deevelopment is a profession dedicated to designing, implementing, modifying software so that it is of higher quality, more affordable, maintainabe, and faster to build. "It is a systematic aproach to the analysis, design, assessment, impementation, test, maintenance and reengineering of software, that is the application of engineering software.</p>
  <a class="more" href="#">Read More...</a>
</article>

<article class="service service--pm">
  <h2>Project Management</h2>
  <p>Project management is the discipline of planning, organising, securing, and managing resources to bring about the successful completion of specific project goals and objectives. It is sometimes conflated programme management, however technically that is actually a higher level construction: a group of relaed and somehow interdependent engineering projects.</p>
  <a class="more" href="#">Read More...</a>
</article>

<article class="service service--consult">
  <h2>Professional Consulting</h2>
  <p>Management consulting indicates both the industry and practise of helping organisations improve their performance primarily through the analysis of existing business problems and development of plans for improvement.<br>Organizations hire the services of management consultants for a number of reasons, including gaining external (and presumably objective) advice and access to the consultants' specialized expertise.</p>
  <a class="more" href="#">Read More...</a>
</article>

<div class="award" role="img" aria-label="Award badge"></div>

<div class="social" aria-label="Social links">
  <span></span><span></span><span></span><span></span><span></span>
</div>

<footer class="footer">Copy Right 2012 Velvet Heron</footer>
</body>
</html>
```